Clean, Fresh Business Card Design Needed

We need a business card design for a new business we have taken over called "Bonders and Fixers". We got a logo through this website which i have attached. We are wanting something that is vibrant but clean and fresh. Our business mainly sells glue. Maybe a cool design/slogan on the back? Modern, sleek.

Industry/Entity Type

Business

Contact Information for Business Card

Name: Derek Tamsin, Managing Director. Address: 164 Kowhai Lane, Marlow Bay 3186, Phone: 07 549 2361 Mobile: 021 634 915 Fax: 07 549 2874 Email: bond.fix@mailvo.co.nz, Web: www.tackbondpro.co.nz

Font styles to use
Serif

Requirements
Must have
• All business card details, logo.
Nice to have
• Design, slogan on back of card

```html
<!DOCTYPE html>
<html lang="en">
<head>
<meta charset="utf-8">
<title>Bonders and Fixers – Business Card</title>
<link rel="stylesheet" href="https://fonts.googleapis.com/css2?family=EB+Garamond:wght@400;600;700&display=swap">
<style>
  :root {
    --stage: #e4e4ea;
    --navy: #2f3270;
    --navy-light: #5a5f9c;
    --band-soft: #6e72aa;
    --card-white: #ffffff;
    --card-fog: #f1f1f4;
    --logo-grey: #6a6a70;
    --ink: #1e1e24;
    --text-grey: #33333a;
    --rule-grey: #a8a8ad;
  }
  * { box-sizing: border-box; margin: 0; padding: 0; }
  html, body {
    width: 1200px; height: 900px; overflow: hidden;
    background: var(--stage);
    font-family: "EB Garamond", Georgia, serif;
  }
  .stage { position: relative; width: 1200px; height: 900px; }
  .card {
    position: absolute; top: 300px;
    width: 510px; height: 300px;
    border-radius: 22px; overflow: hidden;
    box-shadow: 0 10px 24px rgba(0,0,0,0.18);
  }

  /* Back of card */
  .card--back {
    left: 70px;
    background: linear-gradient(160deg, var(--navy) 0%, #3d4080 55%, var(--navy-light) 100%);
    color: var(--card-white);
  }
  .card--back .brand {
    position: absolute; left: 78px; top: 108px;
    display: flex; align-items: center; gap: 16px;
  }
  .card--back .brand-mark {
    width: 64px; height: 64px; border-radius: 6px;
    background: var(--card-white);
  }
  .card--back .brand-name {
    font-size: 31px; font-weight: 400; line-height: 1.0;
    letter-spacing: 0.06em; text-transform: uppercase; color: var(--card-white);
  }
  .card--back .web {
    position: absolute; left: 172px; top: 192px;
    font-size: 15px; letter-spacing: 0.12em; color: var(--card-white);
  }

  /* Front of card */
  .card--front {
    left: 620px;
    background: linear-gradient(180deg, var(--card-fog) 0%, var(--card-white) 45%);
    color: var(--ink);
  }
  .card--front .brand {
    position: absolute; left: 34px; top: 28px;
    display: flex; align-items: center; gap: 14px;
  }
  .card--front .brand-mark {
    width: 70px; height: 70px; border-radius: 6px;
    background: var(--navy);
  }
  .card--front .brand-name {
    font-size: 34px; font-weight: 400; line-height: 1.0;
    letter-spacing: 0.06em; text-transform: uppercase; color: var(--logo-grey);
  }
  .name-band {
    position: absolute; left: 0; top: 122px; width: 100%; height: 32px;
    background: linear-gradient(90deg, var(--band-soft) 0%, var(--navy-light) 45%, var(--navy) 100%);
    display: flex; align-items: baseline; gap: 10px; padding: 4px 0 0 30px;
  }
  .name-band::after {
    content: ""; position: absolute; left: 0; right: 0; bottom: -9px;
    height: 3px; background: var(--rule-grey);
  }
  .person { font-size: 20px; font-weight: 700; color: var(--card-white); }
  .role { font-size: 14px; letter-spacing: 0.08em; color: var(--card-white); }

  .details { position: absolute; left: 30px; top: 180px; }
  .company { font-size: 16px; font-weight: 700; color: var(--text-grey); }
  .address { font-size: 15px; color: var(--text-grey); margin-top: 2px; }
  .contacts {
    list-style: none; margin-top: 12px;
    display: grid; grid-template-columns: 140px 210px; row-gap: 4px; column-gap: 30px;
    font-size: 15px;
  }
  .contacts li { display: flex; align-items: center; gap: 10px; }
  .contacts svg { width: 14px; height: 14px; fill: var(--navy); flex: none; }
</style>
</head>
<body>
<main class="stage">

  <section class="card card--back" aria-label="Card back">
    <div class="brand">
      <span class="brand-mark"></span>
      <span class="brand-name">Bonders<br>and Fixers</span>
    </div>
    <p class="web">www.tackbondpro.co.nz</p>
  </section>

  <section class="card card--front" aria-label="Card front">
    <div class="brand">
      <span class="brand-mark"></span>
      <span class="brand-name">Bonders<br>and Fixers</span>
    </div>

    <div class="name-band">
      <span class="person">Derek Tamsin</span>
      <span class="role">MANAGER</span>
    </div>

    <div class="details">
      <p class="company">Bonders and Fixers</p>
      <p class="address">164 Kowhai Lane, Marlow Bay 3186</p>
      <ul class="contacts">
        <li>
          <svg viewBox="0 0 16 16" aria-label="Phone"><path d="M3 1l3 3-1.5 2a9 9 0 0 0 5.5 5.5L12 10l3 3-2 2C7 15 1 9 1 3z"/></svg>
          07 549 2361
        </li>
        <li>
          <svg viewBox="0 0 16 16" aria-label="Mobile"><path d="M4 0h8v16H4z M5.5 2v10h5V2z"/></svg>
          021 634 915
        </li>
        <li>
          <svg viewBox="0 0 16 16" aria-label="Fax"><path d="M4 1h8v4H4z M1 6h14v7h-3v2H4v-2H1z M5 10v4h6v-4z"/></svg>
          07 549 2874
        </li>
        <li>
          <svg viewBox="0 0 16 16" aria-label="Email"><path d="M1 3h14v10H1z M1.5 3.5L8 9l6.5-5.5" stroke="#fff" stroke-width="1.2"/></svg>
          bond.fix@mailvo.co.nz
        </li>
      </ul>
    </div>
  </section>

</main>
</body>
</html>
```